TK Stationary Design

Logo, Business Card, Letterhead & Email Signature Design

Target Market(s)

Legal

Colors

Designer to choose colors to be used in the design.

Requirements
Must have
• Gold and Blue are the colours to use. The TK must be inside the Gold Legal Pendulum

```html
<!DOCTYPE html>
<html lang="en">
<head>
<meta charset="utf-8">
<title>TK Kgosana Incorporated – Stationery</title>
<link href="https://fonts.googleapis.com/css2?family=Heebo:wght@400;500;700&display=swap" rel="stylesheet">
<style>
  :root{
    --backdrop:#52535b;
    --card:#23242c;
    --card-deep:#1b1c23;
    --gold:#d7b65e;
    --blue:#2443ad;
    --navy:#13236e;
    --ink:#2a2a2a;
    --white:#ffffff;
  }
  *{margin:0;padding:0;box-sizing:border-box}
  html,body{width:1200px;height:900px;overflow:hidden}
  body{background:var(--backdrop);font-family:'Heebo',Arial,sans-serif;position:relative}

  .brand{display:flex;align-items:center;gap:6px;color:var(--gold);font-family:'Heebo',Arial,sans-serif;font-weight:700;letter-spacing:.06em;line-height:1.15;text-transform:uppercase}
  .brand-dot{border-radius:50%;background:var(--gold);flex:none}
  .brand-name{display:flex;flex-direction:column}

  .icon{width:1em;height:1em;flex:none;fill:var(--gold)}
  .contact-list{list-style:none}
  .contact-list li{display:flex;align-items:center;gap:.6em}

  /* Letterhead */
  .letterhead{position:absolute;left:120px;top:52px;width:380px;height:538px;background:var(--white)}
  .letterhead .brand{position:absolute;left:18px;top:34px;font-size:8.5px}
  .letterhead .brand-dot{width:16px;height:16px}
  .letterhead-contact{position:absolute;left:270px;top:30px;font-size:6.4px;color:var(--ink);line-height:1.4}
  .letterhead-contact address{font-style:normal;margin-bottom:4px}
  .letterhead-contact .icon{fill:var(--blue)}
  .letterhead-footer{position:absolute;left:0;bottom:0;width:100%;height:29px;background:linear-gradient(90deg,var(--blue),var(--navy));color:var(--white);font-size:7px;font-weight:700;display:flex;align-items:center;justify-content:center}

  /* Business cards */
  .card{position:absolute;background:var(--card);color:var(--white)}
  .card-front{left:622px;top:80px;width:394px;height:226px}
  .card-front .brand{position:absolute;right:16px;top:56px;font-size:12px}
  .card-front .brand-dot{width:22px;height:22px}
  .card-holder{position:absolute;left:14px;top:114px}
  .holder-name{color:var(--gold);font-size:17px;font-weight:500;line-height:1.1}
  .holder-role{font-size:11px;margin-top:3px}
  .card-rule{position:absolute;left:14px;right:14px;top:157px;height:1px;background:var(--gold)}
  .card-front .contact-list{position:absolute;left:14px;top:167px;font-size:11.5px;line-height:1.45}
  .card-front address{position:absolute;right:14px;top:169px;font-style:normal;text-align:right;font-size:11.5px;line-height:1.4}

  .card-back{left:622px;top:385px;width:392px;height:212px;display:flex;align-items:center;justify-content:center}
  .card-back .brand{font-size:17px;gap:10px}
  .card-back .brand-dot{width:30px;height:30px}

  /* Email signature */
  .signature{position:absolute;left:272px;top:694px;width:614px;height:141px;background:var(--card-deep);color:var(--white);border-bottom:3px solid var(--gold)}
  .signature-photo{position:absolute;left:36px;top:14px;width:108px;height:108px;border-radius:50%;border:3px solid var(--gold);background:radial-gradient(circle at 50% 40%,#dbe5ef,#9fb1c8 70%,#2c3a63)}
  .signature .brand{position:absolute;left:180px;top:30px;font-size:10px}
  .signature .brand-dot{width:16px;height:16px}
  .signature-holder{position:absolute;left:181px;top:96px}
  .signature-holder .holder-name{font-size:16px}
  .signature-holder .holder-role{font-size:11.5px;margin-top:1px}
  .signature .contact-list{position:absolute;left:364px;top:40px;font-size:13px;line-height:1.45}
  .social{position:absolute;left:363px;top:112px;display:flex;align-items:center;gap:9px}
  .social-label{color:var(--gold);font-size:14px;font-weight:500;margin-right:3px}
  .social-dot{width:19px;height:19px;border-radius:50%;background:var(--gold)}
</style>
</head>
<body>

<svg width="0" height="0" style="position:absolute" aria-hidden="true">
  <symbol id="i-phone" viewBox="0 0 24 24"><path d="M6.6 10.8a15.1 15.1 0 0 0 6.6 6.6l2.2-2.2c.3-.3.7-.4 1-.2 1.1.4 2.3.6 3.6.6.6 0 1 .4 1 1V20c0 .6-.4 1-1 1A17 17 0 0 1 3 4c0-.6.4-1 1-1h3.5c.6 0 1 .4 1 1 0 1.3.2 2.5.6 3.6.1.3 0 .7-.2 1z"/></symbol>
  <symbol id="i-fax" viewBox="0 0 24 24"><path d="M6 2h12v5H6zM3 8h18a1 1 0 0 1 1 1v8h-4v5H6v-5H2V9a1 1 0 0 1 1-1zm5 7v5h8v-5z"/></symbol>
  <symbol id="i-mail" viewBox="0 0 24 24"><path d="M2 5h20v14H2zm2 2v.5l8 5 8-5V7l-8 5z"/></symbol>
</svg>

<section class="letterhead">
  <div class="brand"><span class="brand-dot"></span><span class="brand-name"><span>TK Kgosana</span><span>Incorporated</span></span></div>
  <div class="letterhead-contact">
    <address>Block C Linden Office Park<br>42 Elmwood road north<br>Rivonia 2128</address>
    <ul class="contact-list">
      <li><svg class="icon"><use href="#i-phone"/></svg>011 555 0182</li>
      <li><svg class="icon"><use href="#i-fax"/></svg>086 555 0147</li>
      <li><svg class="icon"><use href="#i-mail"/></svg>info@tkkgosana.co.za</li>
    </ul>
  </div>
  <footer class="letterhead-footer">Director: Thabo Kabelo Kgosana BA (NUC), LLB (CSU) and HDip Tax Law (MTU)</footer>
</section>

<section class="card card-front">
  <div class="brand"><span class="brand-dot"></span><span class="brand-name"><span>TK Kgosana</span><span>Incorporated</span></span></div>
  <div class="card-holder">
    <p class="holder-name">Thabo Kgosana</p>
    <p class="holder-role">Director</p>
  </div>
  <div class="card-rule"></div>
  <ul class="contact-list">
    <li><svg class="icon"><use href="#i-phone"/></svg>011 555 0182</li>
    <li><svg class="icon"><use href="#i-fax"/></svg>086 555 0147</li>
    <li><svg class="icon"><use href="#i-mail"/></svg>info@tkkgosana.co.za</li>
  </ul>
  <address>Block C Linden Office Park<br>42 Elmwood road north<br>Rivonia, 2128</address>
</section>

<section class="card card-back">
  <div class="brand"><span class="brand-dot"></span><span class="brand-name"><span>TK Kgosana</span><span>Incorporated</span></span></div>
</section>

<section class="signature">
  <div class="signature-photo" role="img" aria-label="Portrait photo of the director"></div>
  <div class="brand"><span class="brand-dot"></span><span class="brand-name"><span>TK Kgosana</span><span>Incorporated</span></span></div>
  <div class="signature-holder">
    <p class="holder-name">Thabo Kgosana</p>
    <p class="holder-role">Director</p>
  </div>
  <ul class="contact-list">
    <li><svg class="icon"><use href="#i-phone"/></svg>011 555 0182</li>
    <li><svg class="icon"><use href="#i-fax"/></svg>086 555 0147</li>
    <li><svg class="icon"><use href="#i-mail"/></svg>info@tkkgosana.co.za</li>
  </ul>
  <div class="social">
    <span class="social-label">Follow Me om:</span>
    <span class="social-dot" aria-label="Social profile"></span>
    <span class="social-dot" aria-label="Social profile"></span>
    <span class="social-dot" aria-label="Social profile"></span>
    <span class="social-dot" aria-label="Social profile"></span>
  </div>
</section>

</body>
</html>
```